metal roofing website

I have several domain names and a website that has been built. I need someone to recreate essentially the same website and change some photos and basic design to create the new sites. I have all of the files and c panel access to the lucky winner. If you can do a good job at a fair price I will have 100's of sites to send to you very soon. I have the site built and have all files just need it recreated on my server. the current site is www.brantlepanelinc.com I am looking to get this done ASAP!!!

```html
<!DOCTYPE html>
<html lang="en">
<head>
<meta charset="utf-8">
<title>Brantle Panel Inc – Services</title>
<link href="https://fonts.googleapis.com/css2?family=Roboto+Condensed:wght@700&family=Roboto:wght@400;500&display=swap" rel="stylesheet">
<style>
:root{
  --red:#b72d23;
  --red-dark:#a5261d;
  --beige:#e8d7c6;
  --ink:#1a1a1a;
  --white:#ffffff;
}
*{box-sizing:border-box;margin:0;padding:0}
html,body{width:682px;height:1200px;overflow:hidden;background:var(--white);font-family:"Roboto",sans-serif;color:var(--ink)}
.page{position:relative;width:682px;height:1200px}
.topbar{height:24px;background:var(--red);display:flex;align-items:center;justify-content:flex-end;padding-right:69px;gap:10px;color:var(--white);font-family:"Roboto Condensed",sans-serif;font-size:9px;font-weight:700}
.topbar .call{display:flex;align-items:center;gap:4px;margin-right:6px}
.dot{width:8px;height:8px;border-radius:50%;background:var(--white)}
.header{height:63px;background:var(--beige);position:relative}
.brand{position:absolute;left:62px;top:20px;display:flex;align-items:center;gap:6px;font-family:"Roboto Condensed",sans-serif;font-weight:700;font-size:14px;color:var(--red);text-transform:uppercase}
.brand .mark{width:16px;height:16px;background:var(--red)}
.nav{position:absolute;left:291px;top:29px;display:flex;gap:10px;font-size:7.5px;letter-spacing:.3px;text-transform:uppercase}
.nav a{color:var(--ink);text-decoration:none}
.nav a.active{color:var(--red)}
.btn-visualizer{position:absolute;left:538px;top:25px;width:75px;height:21px;border-radius:11px;background:var(--red);color:var(--white);font-size:7.5px;letter-spacing:.4px;display:flex;align-items:center;justify-content:center;text-transform:uppercase}
.hero{height:97px;background:linear-gradient(100deg,#b7382c,#cc5a4c 45%,#c04436);position:relative}
.btn-quote{position:absolute;left:536px;top:41px;width:77px;height:25px;border:1.5px solid var(--white);color:var(--white);font-size:10px;font-weight:500;display:flex;align-items:center;justify-content:center}
h1,h2,h3{font-family:"Roboto Condensed",sans-serif;font-weight:700;color:var(--red);text-transform:uppercase}
.abs{position:absolute}
.title{left:61px;top:228px;font-size:16px}
.deliver h2{font-size:11px;letter-spacing:.4px}
.deliver{left:61px;top:282px;width:400px}
.deliver p{font-size:7px;margin-top:8px}
.call-line{display:flex;align-items:center;gap:12px;margin-top:14px}
.call-line h3{font-size:11px;letter-spacing:.6px}
.photo{position:absolute}
.divider{left:61px;top:394px;width:552px;height:1px;background:#c8868a}
.card{position:absolute;width:261px}
.card .photo{position:static;width:261px;height:196px}
.card h3{font-size:11px;letter-spacing:.4px;margin-top:17px}
.card p{font-size:7px;margin-top:8px}
.footer{position:absolute;left:0;top:996px;width:682px;height:175px;background:var(--beige)}
.fcol{position:absolute;top:36px;font-size:7px;line-height:1.3}
.fcol h3{font-size:9px;letter-spacing:.4px;margin-bottom:9px}
.fcol p{margin-bottom:2px}
.fcol ul{list-style:none}
.fcol li{margin-bottom:7px;padding-left:7px;position:relative}
.fcol li::before{content:"";position:absolute;left:0;top:1px;width:3px;height:3px;border-radius:50%;background:var(--red)}
.bottombar{position:absolute;left:0;top:1171px;width:682px;height:29px;background:var(--red);color:var(--white);font-size:7px;font-weight:500;display:flex;align-items:center;justify-content:space-between;padding:0 69px 0 61px}
.bottombar .social{display:flex;gap:12px}
</style>
</head>
<body>
<div class="page">
  <div class="topbar">
    <span class="call">
      <svg width="6" height="9" viewBox="0 0 6 9"><rect x=".5" y=".5" width="5" height="8" rx="1" fill="none" stroke="#fff"/><rect x="2" y="7" width="2" height=".8" fill="#fff"/></svg>
      Call US: 555-210-4471
    </span>
    <span class="dot"></span><span class="dot"></span><span class="dot"></span>
  </div>
  <header class="header">
    <div class="brand"><span class="mark"></span>Brantle Panel Inc</div>
    <nav class="nav">
      <a href="#">Home</a><a href="#">About Us</a><a href="#" class="active">Services</a><a href="#">Gallery</a><a href="#">Contact Us</a>
    </nav>
    <div class="btn-visualizer">Visualizer</div>
  </header>
  <section class="hero" role="img" aria-label="Red-tinted photo of a barn roof with dormers and a cupola">
    <div class="btn-quote">GET QUOTE</div>
  </section>

  <h1 class="abs title">Services</h1>
  <div class="abs deliver">
    <h2>We can deliver</h2>
    <p>Ask our Sales Team about our delivery and unloading options.</p>
    <div class="call-line">
      <svg width="10" height="17" viewBox="0 0 10 17"><rect x="1" y="1" width="8" height="15" rx="1.5" fill="none" stroke="#1a1a1a" stroke-width="1.6"/><rect x="3.5" y="13" width="3" height="1.2" fill="#1a1a1a"/></svg>
      <h3>Call us : 555-210-4471</h3>
    </div>
  </div>
  <div class="photo" style="left:498px;top:281px;width:115px;height:86px;background:linear-gradient(#9fb3c8,#c9ccd0 45%,#8a8c8e)" role="img" aria-label="Delivery truck loaded with metal panels and a forklift outside the warehouse"></div>
  <div class="abs divider"></div>

  <div class="card" style="left:61px;top:434px">
    <div class="photo" style="background:linear-gradient(#4a86d6 0%,#8fb3e0 30%,#9a9a96 55%,#7a6a55 85%,#3f3a30)" role="img" aria-label="Large grey post frame building on cleared dirt"></div>
    <h3>Complete post frame building packages</h3>
    <p>Call us for a quote, or stop in and we can help you design</p>
  </div>
  <div class="card" style="left:352px;top:434px">
    <div class="photo" style="background:linear-gradient(#c9cdc8,#6f7a66 35%,#7a3a2e 60%,#5d7a3a 85%,#b9bcb8)" role="img" aria-label="Red house with grey metal roof among trees"></div>
    <h3>Residential metal roofing</h3>
    <p>Super rib, snap-loc and a variety of metal roofing options.</p>
  </div>
  <div class="card" style="left:61px;top:708px">
    <div class="photo" style="background:linear-gradient(#e4e6e8,#d8cdb4 35%,#8a3a3a 62%,#a9a8a4 75%,#7d7c78)" role="img" aria-label="Cream commercial barn with maroon gambrel roof and grain bins"></div>
    <h3>Commercial applications</h3>
    <p>28 gauge panels are the thickest and strongest in the industry.</p>
  </div>
  <div class="card" style="left:352px;top:708px">
    <div class="photo" style="background:linear-gradient(#8a9096,#b8bcc0 35%,#a83a34 58%,#6a5f52 80%,#4c443a)" role="img" aria-label="Agricultural building with red walls and white overhead doors"></div>
    <h3>Agricultural applications</h3>
    <p>28 gauge panels are the thickest and strongest in the industry.</p>
  </div>

  <footer class="footer">
    <div class="fcol" style="left:61px">
      <h3>Brantle Panel Inc</h3>
      <p>Phone:</p><p style="margin-bottom:12px">555-210-4470</p>
      <p>Fax:</p><p>555-210-4471</p>
    </div>
    <div class="fcol" style="left:255px">
      <h3>Sitemap</h3>
      <ul><li>Home</li><li>About Us</li><li>Services</li><li>Gallery</li><li>Contact Us</li></ul>
    </div>
    <div class="fcol" style="left:449px;line-height:2.1">
      <h3 style="line-height:1.3">Hours</h3>
      <p style="margin:0">Monday – Friday: 7am – 5pm</p>
      <p style="margin:0">Saturday: 7am – 12pm</p>
      <p style="margin:0">Sunday: Closed</p>
    </div>
  </footer>
  <div class="bottombar">
    <span>Copyright © 2018 Brantle Panel Inc. All rights reserved.</span>
    <span class="social"><span class="dot"></span><span class="dot"></span><span class="dot"></span></span>
  </div>
</div>
</body>
</html>
```